Environmental and Industrial Services Company Needs Brochure Design

We need a new brochure design for an established company that services the Southeastern United States. It is a highly diversified company that centers around Environmental and Industrial Services. The Environmental side revolved around emergency chemical and spill response, HAZMAT, hazardous/ non hazardous waste management, wastewater treatment, and remediation services (cleaning up contaminated sites). And the Industrial side utilizes heavy equipment like vacuum trucks and hydroblasters to clean process equipment inside of factories and manufacturing facilities. Predominantly our clients are large industrial clients, commercial clients, and the government. The people who would see the brochure are decision makers; engineers, project managers, procurement heads for large companies. These are serious and educated people who are looking for the best.

The designs should incorporate our colors and I welcome you to use any of the pictures from our website www.kvlterra.com EXCLUSIVELY FOR THIS PROJECT, of course. This brochure should communicate professionalism, confidence, stability, and portray the kind of company who efficiently manages complicated issues. Our site gives a better kind of idea of the branding we want to extend into the brochure and I caution any designer to NOT allow the environmental aspect of our company to lead them to design brochures more fitting for Green Tech companies or Alternative Energy.

Target Market(s)

Engineers, Factory Managers, Project Managers, Consultants, Heads of Large Companies, Service Managers

Industry/Entity Type

Industrial

Requirements
Must have
• The brochure must
-Be divided like the services section of our website w/ categories in this order:
-Industrial Services, Waste Management, Remediation Services, Emergency Response, Marine Services, Stormwater Services
-Owing to the large info in these sections, I'd recommend separate pages or tabs
-Incorporate our colors
-Use photos from the site

```html
<!DOCTYPE html>
<html lang="en">
<head>
<meta charset="utf-8">
<title>KVL Terra Brochure</title>
<link href="https://fonts.googleapis.com/css2?family=Source+Sans+3:wght@400;600;700&family=Crimson+Text:wght@400;600&display=swap" rel="stylesheet">
<style>
:root{
  --brand-blue:#1f4c8f;
  --emboss:#15376a;
  --heading-blue:#1d4f91;
  --ink:#2a2a2a;
  --paper:#ffffff;
  --panel-grey:#eceeee;
  --tint:#cfdcef;
  --bg:#ffffff;
}
*{margin:0;padding:0;box-sizing:border-box}
html,body{width:1200px;height:900px;overflow:hidden;background:var(--bg)}
body{position:relative;font-family:"Crimson Text",Georgia,serif;color:var(--ink)}

/* Cover */
.cover{position:absolute;left:20px;top:20px;width:700px;height:470px;background:var(--brand-blue);box-shadow:0 4px 10px rgba(0,0,0,.25)}
.cover-title{position:absolute;font-family:"Source Sans 3",Arial,sans-serif;font-weight:700;color:var(--emboss);font-size:27px;letter-spacing:.5px;white-space:nowrap;line-height:1}
.cover-title small{font-size:18px;font-weight:600}
.brand-name{position:absolute;font-family:"Source Sans 3",Arial,sans-serif;font-weight:700;color:#fff;display:flex;align-items:center;gap:6px;line-height:1;white-space:nowrap}
.brand-name .sq{display:inline-block;background:currentColor}
.cover-contact{position:absolute;left:125px;top:418px;color:#fff;font-family:"Source Sans 3",Arial,sans-serif;font-weight:700;font-size:13px;line-height:20px}

/* Spread */
.spread{position:absolute;left:475px;top:385px;width:700px;height:500px;background:var(--brand-blue);box-shadow:0 4px 12px rgba(0,0,0,.3);overflow:hidden}
.panel{position:absolute;background:var(--paper)}
.panel-left{left:8px;top:6px;width:225px;height:440px;border-top-right-radius:60px;border-bottom-right-radius:60px}
.panel-center{left:240px;top:0;width:245px;height:440px;border-bottom-right-radius:70px}
.panel-right{left:488px;top:96px;width:212px;height:404px;background:var(--panel-grey);border-top-left-radius:40px}
.photo{position:absolute}

.col{position:absolute;display:flex;flex-direction:column;gap:4px;overflow:hidden}
.h2{font-family:"Source Sans 3",Arial,sans-serif;font-weight:700;color:var(--heading-blue);font-size:9px;line-height:1.1}
.h2.center{text-align:center}
.body{font-size:5.8px;line-height:1.25;text-align:justify}
.list{font-size:5.4px;line-height:1.25;list-style:none}
.list li::before{content:"• "}
.dropcap::first-letter{float:left;font-size:20px;line-height:16px;color:var(--heading-blue);padding-right:2px}
.callout{float:left;width:52px;margin:1px 4px 2px 0;background:var(--tint);color:var(--heading-blue);font-family:"Source Sans 3",Arial,sans-serif;font-weight:600;font-size:6.4px;line-height:1.15;padding:3px;text-align:left}
.inline-photo{float:right;border-radius:50%;margin:0 0 2px 4px}
</style>
</head>
<body>

<section class="cover" aria-label="Folder cover">
  <div class="cover-title" style="left:338px;top:74px">SIMPLE SOLUTIONS</div>
  <div class="cover-title" style="left:408px;top:240px"><small>to</small> COMPLEX PROBLEMS</div>
  <div class="brand-name" style="left:105px;top:322px;font-size:24px"><span class="sq" style="width:22px;height:22px"></span>KVL TERRA</div>
  <div class="cover-contact">(910) 555-0148<br>www.kvlterra.com</div>
</section>

<section class="spread" aria-label="Brochure inside spread">
  <!-- Left page -->
  <div class="panel panel-left"></div>
  <div class="photo" role="img" aria-label="Industrial plant piping and steel structure" style="left:12px;top:6px;width:205px;height:58px;border-top-right-radius:50px;background:linear-gradient(135deg,#8fb6d9,#c9a24a 55%,#3b5c78)"></div>

  <div class="col waste-col" style="left:16px;top:72px;width:100px;height:276px">
    <div class="h2 center">Waste Management</div>
    <p class="body">KVL Terra provides transportation, recycling, and disposal of all types of hazardous and non-hazardous wastes. Our team is able to analyze, categorize, and then handle waste in the safest and most efficient way using up-to-date methods. Our recycling program keeps waste out of landfills and turns used oil back into usable product.</p>
    <p class="body">For more information on how KVL Terra can help you with your waste, please contact us.</p>
    <div class="h2 center">Waste categories:</div>
    <ul class="list">
      <li>Liquids, solids, sludges, and residuals</li><li>Hazardous and non-hazardous</li><li>Lab Packs</li><li>Drums</li><li>Totes</li><li>Roll offs</li><li>Byproducts</li><li>Used oil and petroleum products</li>
    </ul>
    <p class="body">KVL Terra will analyze your waste stream and determine which treatment will be most effective. Whether it needs to be stabilized, solidified, blended, or treated in our wastewater system, we can find a unique solution.</p>
  </div>

  <div class="col remediation-col" style="left:124px;top:72px;width:100px;height:276px">
    <div class="h2 center">Remediation</div>
    <p class="body"><span class="photo inline-photo" role="img" aria-label="Excavator working a site" style="position:static;display:block;width:26px;height:26px;background:radial-gradient(#c9a640,#6d6a55)"></span>Thanks to modern life, contamination is inevitable. But it isn't untreatable. Our state-of-the-art remediation methods let us take on any job, from a residential storage tank to a superfund site.</p>
    <p class="body">Our clients know a mishandled remediation only exposes them to more liability. That's why they rely on our turn-key services to keep every site in line with local, state, and federal rules.</p>
    <div class="h2 center">Here's a sampling of how KVL Terra can help with your remediation efforts:</div>
    <ul class="list">
      <li>Contaminated Soil and Groundwater</li><li>UST Closure and Excavation</li><li>Aggressive Fluid Vapor Recovery</li><li>Facility Decommissioning</li><li>Demolition</li><li>Biohazard cleanup</li><li>Storage Tanks</li><li>Excavation and grading</li><li>Bioremediation</li><li>Lab Packing</li><li>Dewatering</li>
    </ul>
  </div>

  <div class="photo" role="img" aria-label="Worker in protective gear pressure washing equipment" style="left:55px;top:352px;width:84px;height:84px;border-radius:50%;background:radial-gradient(#c9c06a,#4d5a66);border:2px solid #fff"></div>
  <div class="photo" role="img" aria-label="Service trucks at a job site" style="left:136px;top:364px;width:84px;height:58px;background:linear-gradient(#b9cde0,#e6e6e6 55%,#6c7a86)"></div>
  <div class="brand-name" style="left:250px;top:456px;font-size:13px"><span class="sq" style="width:12px;height:12px"></span>KVL TERRA</div>

  <!-- Center page -->
  <div class="panel panel-center"></div>
  <div class="col industrial-col" style="left:248px;top:8px;width:110px;height:428px">
    <div class="h2 center">Industrial Services</div>
    <p class="body dropcap">KVL Terra's Industrial Services Division is the hardest working team in the business. We're at work 24 hours a day, 365 days a year in a diverse array of facilities across the Southeast. For over 20 years, we've safely performed all facets of industrial cleaning. With the equipment of a large company and the care of a small one, we get the job done right the first time. No more worrying about accidents, hidden fees or the dreaded "change order." Just your project done right.</p>
    <div class="h2 center">Here's a partial overview of our capabilities:</div>
    <ul class="list">
      <li>Vacuum Truck Service</li><li>Sump/Pit Cleaning</li><li>Oil-water separator maintenance</li><li>Bulk solids and ash handling</li><li>Aggressive Fluid Vapor Recovery</li><li>Liquids vacuum transfer</li><li>Liquids and solids transportation</li><li>Hydroblasting Services</li><li>No entry (3D tool) tank cleaning</li><li>Interior and exterior surfaces</li><li>Tank, reactor, and vessel cleaning</li><li>Tube and process pipe "lancing"</li><li>Heat exchanger cleaning</li><li>Underground drainage lines</li><li>Facility decontamination</li><li>Tank and Line Cleaning</li><li>Scheduled/Emergency shut downs</li><li>Cooling towers</li><li>Drain and sump cleanout</li><li>Oil-water separators</li><li>Pond/lagoon dredging</li><li>Material Removal</li><li>Solidification</li><li>Stabilization</li><li>Wastewater Treatment</li><li>Waste Transportation</li>
    </ul>
  </div>

  <div class="col reputation-col" style="left:366px;top:10px;width:114px;height:368px">
    <div class="h2 center">An Unmatched Reputation</div>
    <p class="body dropcap">For more than 20 years, KVL Terra has cultivated an unmatched reputation for safety, professionalism, and service excellence.</p>
    <p class="body">Today we stand as an industry leader in industrial cleaning, spill response, remediation, and waste management across the Southeast.</p>
    <p class="body dropcap">The Kestrel Valley Response and Remediation was founded in 1991 in response to the growing number of oil and chemical spills in Eastern North Carolina.</p>
    <p class="body">Our original mission was to provide a safe and cost-effective way to handle these spills. This focus quickly grew to a broad spectrum of environmental services and a thriving Industrial Services division.</p>
    <p class="body"><span class="callout">We're at work 24 hours a day, 365 days a year in a diverse array of facilities across the Southeast.</span>Though KVL Terra has grown and diversified, we've kept true to our belief that "Bigger can't be better. Better is better." We still provide the same emergency response services that earned our reputation, an industry-leading safety record and first-class training. After two decades we're known for so much more than emergency response.</p>
  </div>
  <div class="photo" role="img" aria-label="Responder in a full hazmat suit" style="left:392px;top:384px;width:90px;height:90px;border-radius:50%;background:radial-gradient(#d8643a,#5a4a44);border:2px solid #fff"></div>

  <!-- Right page -->
  <div class="photo" role="img" aria-label="Rows of rusted waste drums" style="left:480px;top:4px;width:220px;height:96px;border-top-left-radius:60px;background:linear-gradient(160deg,#b8542c,#8a6a3c 50%,#c0392b)"></div>
  <div class="panel panel-right"></div>

  <div class="col safety-col" style="left:495px;top:108px;width:95px;height:302px">
    <div class="h2 center">Safety</div>
    <p class="body">No two jobs are alike, but one thing is the same every time: our commitment to safety. Each employee has, at a minimum, the following training before going to a client's site:</p>
    <ul class="list">
      <li>HAZWOPER – 40hr</li><li>Confined Space</li><li>CPR</li><li>First Aid</li><li>Vacuum Truck Operation</li><li>Basic Skills Training</li><li>Client Site Specific Training</li><li>Background Checks</li>
    </ul>
    <p class="body">Certifications are kept through third-party instructors and our own training staff.</p>
    <div class="h2 center" style="margin-top:4px">Stormwater Services</div>
    <p class="body">Let us take care of all your sewer jetting and pipe cleaning needs:</p>
    <ul class="list">
      <li>Culvert and manhole cleaning</li><li>Pipeline video inspection</li><li>Sewer line cleaning</li><li>Lift stations</li><li>Pits and trenches</li><li>Sand filters and process tanks</li><li>Underground cisterns</li>
    </ul>
  </div>

  <div class="col response-col" style="left:601px;top:108px;width:95px;height:302px">
    <div class="h2 center">Emergency Response</div>
    <p class="body"><span class="photo inline-photo" role="img" aria-label="Boom deployed on water" style="position:static;display:block;width:24px;height:24px;background:radial-gradient(#9aa6ad,#4e5a60)"></span>Accidents happen... So do spills. KVL Terra is the best at handling the worst, from small biohazard sites to large oil and chemical discharges. As a licensed Oil Spill Removal Organization (OSRO), we respond on land and water. When it has to be right now, call us.</p>
    <ul class="list">
      <li>24 hour response, water or land</li><li>Petroleum and chemical spills</li><li>Biohazard cleanup</li><li>Industrial Accidents</li><li>Transportation Spills</li><li>Licensed OSRO</li><li>Training and drills</li>
    </ul>
    <div class="h2 center" style="margin-top:4px">Marine Services</div>
    <p class="body">Marine work is a specialized field. Our team knows how to safely handle its risks.</p>
    <ul class="list">
      <li>Mobile Transfer Facility</li><li>AMPD Coverage</li><li>Slops and Fuel Removal</li><li>Bilge Cleaning/Decon</li><li>Sunken Vessel Service</li><li>MARPOL Coverage</li><li>OSRO Coverage</li><li>Booming</li><li>Pressure Washing</li>
    </ul>
  </div>

  <div class="photo" role="img" aria-label="Crews cleaning a drainage ditch" style="left:560px;top:414px;width:44px;height:56px;background:linear-gradient(#a9bccb,#6f7d68)"></div>
  <div class="photo" role="img" aria-label="Debris along a shoreline" style="left:606px;top:414px;width:40px;height:56px;background:linear-gradient(#b4bfc6,#5d5a4e)"></div>
  <div class="photo" role="img" aria-label="Response vessel at a dock" style="left:648px;top:414px;width:52px;height:56px;background:linear-gradient(#c4d2dc,#2c3a4a 60%,#8a3a2a)"></div>
  <div class="brand-name" style="left:624px;top:480px;font-size:11px;color:var(--brand-blue)"><span class="sq" style="width:10px;height:10px"></span>KVL TERRA</div>
</section>

</body>
</html>
```